Letterhead to coordinate with business card

I am needing a docx template and print file for a letterhead to co-ordinate with my newly designed logo and business card.

```html
<!DOCTYPE html>
<html lang="en">
<head>
<meta charset="utf-8">
<title>Harbourline Plan Services – Letterhead</title>
<link rel="stylesheet" href="https://fonts.googleapis.com/css2?family=Arimo:wght@400&display=swap">
<style>
  :root {
    --backdrop: #d9dadd;
    --paper: #ffffff;
    --paper-shade: #ececec;
    --slate: #2e3440;
    --berry: #a83266;
    --teal: #007f7c;
    --ink: #1c1c1c;
  }
  * { margin: 0; padding: 0; box-sizing: border-box; }
  html, body {
    width: 1200px; height: 1141px; overflow: hidden;
    background: var(--backdrop);
    font-family: "Arimo", Arial, sans-serif;
  }
  .sheet-frame {
    position: absolute; left: 209px; top: 20px;
    width: 783px; height: 1100px;
  }
  .letterhead {
    position: absolute; left: 0; top: 0;
    width: 1012px; height: 1422px;
    transform: scale(0.7736); transform-origin: 0 0;
    background: linear-gradient(160deg, var(--paper) 45%, var(--paper-shade) 100%);
  }
  .side-panel { position: absolute; left: 0; top: 0; width: 1012px; height: 1422px; }
  .grad-slate { stop-color: var(--slate); }
  .grad-berry { stop-color: var(--berry); }
  .grad-teal { stop-color: var(--teal); }

  .brand {
    position: absolute; left: 195px; top: 74px; width: 220px;
    display: flex; flex-direction: column; align-items: center; gap: 14px;
  }
  .brand-square { width: 64px; height: 64px; background: var(--teal); }
  .brand-name {
    color: var(--berry); font-size: 24px; line-height: 1.15;
    text-align: center;
  }

  .contact {
    position: absolute; right: 60px; top: 78px;
    color: var(--ink); font-size: 17px; line-height: 21px;
    text-align: right;
  }
  .contact-group { margin-bottom: 7px; }
  .contact-line { display: flex; justify-content: flex-end; align-items: center; gap: 12px; white-space: nowrap; }
  .contact-line .icon { width: 14px; height: 14px; flex: none; }
  .icon-spacer { width: 14px; flex: none; }
  .icon path, .icon circle { fill: var(--teal); }
</style>
</head>
<body>
  <div class="sheet-frame">
    <div class="letterhead">
      <svg class="side-panel" viewBox="0 0 1012 1422" role="img" aria-label="Decorative sweeping band in slate, berry and teal along the left edge">
        <defs>
          <linearGradient id="panel-tones" x1="0" y1="0" x2="1" y2="1">
            <stop offset="0" class="grad-slate"/>
            <stop offset="0.55" class="grad-slate"/>
            <stop offset="0.8" class="grad-berry"/>
            <stop offset="1" class="grad-teal"/>
          </linearGradient>
        </defs>
        <path fill="url(#panel-tones)" d="M0,0 H243 C90,400 70,1000 177,1422 H0 Z"/>
      </svg>

      <div class="brand">
        <div class="brand-square"></div>
        <div class="brand-name">Harbourline Plan Services</div>
      </div>

      <div class="contact">
        <div class="contact-group">
          <div class="contact-line"><span>Harbourline Plan Services</span>
            <svg class="icon" viewBox="0 0 14 14"><path d="M7,0 C3.8,0 1.8,2.3 1.8,5 C1.8,8.5 7,14 7,14 C7,14 12.2,8.5 12.2,5 C12.2,2.3 10.2,0 7,0 Z M7,3 A2,2 0 1 1 7,7 A2,2 0 1 1 7,3 Z"/></svg>
          </div>
          <div class="contact-line"><span>PO Box 482</span><span class="icon-spacer"></span></div>
          <div class="contact-line"><span>Kelvin Grove NSW 2391</span><span class="icon-spacer"></span></div>
        </div>
        <div class="contact-line"><span>0400 318 576</span>
          <svg class="icon" viewBox="0 0 14 14"><path d="M2.5,0.5 L5,0.5 L6,4 L4.3,5.2 C5.2,7.2 6.8,8.8 8.8,9.7 L10,8 L13.5,9 L13.5,11.5 C13.5,12.6 12.6,13.5 11.5,13.5 C5.5,13.2 0.8,8.5 0.5,2.5 C0.5,1.4 1.4,0.5 2.5,0.5 Z"/></svg>
        </div>
        <div class="contact-line"><span>hello@harbourlineplans.com.au</span>
          <svg class="icon" viewBox="0 0 14 14"><path d="M1,3 H13 V11 H1 Z M2,4 L7,7.5 L12,4 Z" fill-rule="evenodd"/></svg>
        </div>
        <div class="contact-line"><span>harbourlineplans.com.au</span>
          <svg class="icon" viewBox="0 0 14 14"><circle cx="7" cy="7" r="6" opacity="0.45"/></svg>
        </div>
      </div>
    </div>
  </div>
</body>
</html>
```